Business Cards Needed For Veterinary Business

Looking for a business card design for a veterinary blood bank. We would like it to be clean and professional on appearance but still warm and inviting. We would like to utilize our logo and similar coloring. We will use our phone number, email, website, employee name, employee title.

We do not want a bunch of animated animal photos but do not need the style to be as clinical as a laboratory or human medical procedure office.

We are looking for some creative ideas to choose from so that we can generate a standout professional business card for our management team to utilize.

Target Market(s)

professionals

Industry/Entity Type

veterinary

Contact Information for Business Card

employee name, employee title, phone number, website URL, email

Font styles to use
Sans Serif

Colors
0054AA
0677BA
7BADD7
CADEEF
E8F1F8
EB3D1F
EC4F4E
F09395
F8D3D4
FCEDEE

Requirements
Nice to have
• creative design
Should not have
• animated photos

```html
<!DOCTYPE html>
<html lang="en">
<head>
<meta charset="utf-8">
<title>Cedarline Veterinary Blood Bank – Business Card</title>
<link href="https://fonts.googleapis.com/css2?family=Montserrat:wght@500;700;800&display=swap" rel="stylesheet">
<style>
  :root{
    --brand-red:#ec1f27;
    --brand-blue:#0e4c96;
    --ink:#1a1a1a;
    --white:#ffffff;
    --stage:#1c1c1c;
  }
  html,body{margin:0;padding:0;overflow:hidden;}
  body{width:1200px;height:1059px;background:var(--stage);position:relative;font-family:"Montserrat",sans-serif;}
  .card{position:absolute;border-radius:22px;overflow:hidden;box-shadow:0 10px 30px rgba(0,0,0,.55);}
  .card-front{left:256px;top:89px;width:688px;height:391px;background:var(--white);}
  .card-back{left:253px;top:546px;width:694px;height:395px;background:var(--brand-red);}
  .wave{position:absolute;left:0;top:0;}
  .brand{position:absolute;display:flex;align-items:center;}
  .brand-front{left:40px;top:58px;gap:16px;}
  .brand-mark{border-radius:50%;flex:none;}
  .brand-front .brand-mark{width:72px;height:72px;background:var(--brand-red);}
  .brand-name{font-weight:800;line-height:1.1;margin:0;text-transform:uppercase;white-space:nowrap;}
  .brand-front .brand-name{color:var(--brand-red);font-size:26px;}
  .person{position:absolute;right:36px;top:138px;text-align:right;}
  .person-name{margin:0;font-weight:700;font-size:24px;color:var(--brand-blue);line-height:1.1;}
  .person-title{margin:2px 0 0;font-weight:500;font-size:14px;color:var(--ink);}
  .accent-bar{position:absolute;right:0;top:143px;width:17px;height:43px;background:var(--brand-red);}
  .contacts{position:absolute;right:36px;top:285px;margin:0;padding:0;list-style:none;}
  .contacts li{display:flex;justify-content:flex-end;align-items:center;gap:10px;height:26px;color:var(--white);font-size:14px;font-weight:500;}
  .contacts svg{width:14px;height:14px;flex:none;}
  .brand-back{left:0;right:0;top:0;bottom:0;justify-content:center;gap:22px;}
  .brand-back .brand-mark{width:104px;height:104px;background:var(--white);}
  .brand-back .brand-name{color:var(--white);font-size:40px;}
</style>
</head>
<body>
  <section class="card card-front">
    <svg class="wave" width="688" height="391" viewBox="0 0 688 391" aria-hidden="true">
      <path d="M0 299 C60 330 110 350 180 346 C300 340 420 270 520 240 C590 222 650 225 688 238 L688 280 C640 265 580 262 510 280 C400 310 290 360 180 354 C110 352 50 340 0 318 Z" fill="var(--brand-blue)"/>
      <path d="M0 322 C60 348 120 360 190 356 C300 350 410 300 510 284 C590 270 650 272 688 284 L688 391 L0 391 Z" fill="var(--brand-red)"/>
    </svg>
    <div class="brand brand-front">
      <span class="brand-mark"></span>
      <p class="brand-name">Cedarline<br>Veterinary<br>Blood Bank</p>
    </div>
    <div class="person">
      <p class="person-name">Jonah Whitfield</p>
      <p class="person-title">Managing Director</p>
    </div>
    <span class="accent-bar"></span>
    <ul class="contacts">
      <li>555-014-2290
        <svg viewBox="0 0 16 16" aria-hidden="true"><path fill="#fff" d="M2 6c0-2 2.5-3 6-3s6 1 6 3v1h-3V5.5H5V7H2z M4 8h8l1.5 6h-11z"/><circle cx="8" cy="11" r="1.6" fill="var(--brand-red)"/></svg></li>
      <li>hello@cedarlinebloodbank.com
        <svg viewBox="0 0 16 16" aria-hidden="true"><rect x="1" y="3" width="14" height="10" rx="1" fill="#fff"/><path d="M1.5 3.8 8 9l6.5-5.2" fill="none" stroke="var(--brand-red)" stroke-width="1.2"/></svg></li>
      <li>www.cedarlinebloodbank.com
        <svg viewBox="0 0 16 16" aria-hidden="true"><circle cx="8" cy="8" r="7" fill="#fff"/><path d="M8 1v14M1 8h14M8 1c-3 3-3 11 0 14M8 1c3 3 3 11 0 14" fill="none" stroke="var(--brand-red)" stroke-width="1"/></svg></li>
    </ul>
  </section>

  <section class="card card-back">
    <div class="brand brand-back">
      <span class="brand-mark"></span>
      <p class="brand-name">Cedarline<br>Veterinary<br>Blood Bank</p>
    </div>
  </section>
</body>
</html>
```